Package Storage Service

Ideas...

Business Name... "TUCK IT AT BRAMWOOD":
Store it,
Don’t Ship it;
4-LESS
Convenience, Quality, Service

Easy as ABC…
A. Contact Us 064-293-5527
B. We deliver
C. We pick-up & Store

LESS, is the new MORE

Box Size* (Approx) Weight Limit Price per Month
41 cm X 34 cm X 26 cm 10 Kilos 12 CHFs/per month
48 cm X 43 cm X 35 cm 25 Kilos 25 CHFs/per month

* Larger sizes and prices available upon request.

Contact: Tom /064-293-5527

These are only ideas for a small package storage service for local college students. The storage times are usually for 1 - 3 months.
I need a catchy, creative, colorful design for a new business.

This flyer will need to be printable in color. A-4 size or 8 1/2 " X 11".

Target Market(s)

Hotel Management students leaving their program for vacations for short terms. They return after vacation or after practical work experiences 4 study.

Industry/Entity Type

College

Requirements
Must have
• Prices, box sizes, catchy format.

Idea will forward to their address should they not return to the school; for a postage fee + 15.00 CHFs.

Contact information for the PICKUP and DELIVERY Service... see above.

Include a PICKUP AND DELIVERY Option in the flyer.
Nice to have
• Colorful boxes with a creative idea for someone to choose spending a little each month rather than a lot at one time. 25 CHFs rather than 125 CHFs.
Should not have
• Not too wordy.

```html
<!DOCTYPE html>
<html lang="en">
<head>
<meta charset="utf-8">
<title>Tuck It At Bramwood – Package Storage Flyer</title>
<link rel="stylesheet" href="https://fonts.googleapis.com/css2?family=Anton&family=Archivo+Black&family=Oswald:wght@500;700&family=Roboto:ital,wght@0,500;0,700;1,900&display=swap">
<style>
  :root {
    --yellow: #e1e31b;
    --black: #000000;
    --white: #ffffff;
    --cyan: #00a6e2;
    --pink: #e6197e;
    --cardboard: #c9a06e;
  }
  * { margin: 0; padding: 0; box-sizing: border-box; }
  html, body { width: 848px; height: 1200px; overflow: hidden; background: var(--white); }
  .flyer {
    position: relative;
    width: 848px;
    height: 1200px;
    overflow: hidden;
    background: var(--black);
    font-family: "Roboto", Arial, sans-serif;
  }
  .headline { position: absolute; left: 0; top: 0; width: 848px; height: 600px; }
  .display { font-family: "Anton", Impact, sans-serif; }
  .display-heavy { stroke: var(--black); stroke-width: 7; stroke-linejoin: round; }

  .with-label {
    position: absolute; left: 74px; top: 568px;
    font: italic 900 20px "Roboto", Arial, sans-serif; color: var(--white);
  }
  .business-name { position: absolute; left: 0; top: 590px; width: 848px; height: 90px; }
  .business-name text { font-family: "Archivo Black", Arial, sans-serif; font-size: 86px; fill: var(--yellow); }
  .business-name .accent { fill: var(--white); }

  .tagline {
    position: absolute; left: 68px; top: 668px; white-space: nowrap;
    font: 500 56px/1 "Roboto", Arial, sans-serif; color: var(--cyan); letter-spacing: -0.3px;
  }
  .forward-note {
    position: absolute; left: 410px; top: 752px; width: 420px; white-space: nowrap;
    font: italic 900 12.5px/1.3 "Roboto", Arial, sans-serif; color: var(--yellow);
    padding-left: 18px;
  }
  .forward-note::before {
    content: "*"; position: absolute; left: 0; top: -3px;
    font-size: 24px; color: var(--white);
  }
  .contact {
    position: absolute; left: 428px; top: 804px; width: 410px;
    font: 700 21px/1.3 "Roboto", Arial, sans-serif; color: var(--white);
  }
  .contact .phone { color: var(--pink); font-size: 36px; font-family: "Oswald", Arial, sans-serif; font-weight: 500; vertical-align: -3px; }
  .contact .sub { display: block; margin-left: 84px; }

  .steps-circle {
    position: absolute; left: -102px; top: 744px; width: 540px; height: 540px;
    border-radius: 50%; background: var(--yellow); border: 9px solid var(--white);
  }
  .steps {
    position: absolute; left: 0; top: 806px; width: 420px; text-align: center;
  }
  .steps-title {
    font: 700 46px/1 "Oswald", Impact, sans-serif; color: var(--black);
    transform: scaleX(0.86); letter-spacing: 1px; margin-left: 34px;
  }
  .step-list { list-style: none; margin-top: 6px; }
  .step-list li {
    font: 700 27px/35px "Roboto", Arial, sans-serif; color: var(--white);
  }
  .step-list .letter { color: var(--black); }
  .slogan {
    margin-top: 14px; white-space: nowrap;
    font: italic 900 37px/1 "Roboto", Arial, sans-serif; color: var(--cyan);
    text-shadow: 3px 3px 3px rgba(0,0,0,0.45); letter-spacing: -0.5px;
  }
  .boxes-photo {
    position: absolute; left: 110px; top: 1030px; width: 360px; height: 170px;
    background: linear-gradient(160deg, #d8b585, var(--cardboard) 55%, #a67a4b);
    clip-path: polygon(18% 14%, 46% 0, 66% 10%, 72% 28%, 86% 36%, 100% 60%, 100% 100%, 0 100%, 0 62%, 16% 50%);
  }

  .sizes-circle {
    position: absolute; left: 430px; top: 900px; width: 460px; height: 460px;
    border-radius: 50%; background: var(--white); border: 9px solid var(--yellow);
  }
  .sizes {
    position: absolute; left: 440px; top: 938px; width: 300px; text-align: center;
  }
  .sizes-title {
    font: 700 40px/1 "Oswald", Impact, sans-serif; color: var(--black);
    transform: scaleX(0.9); white-space: nowrap;
  }
  .sizes-title sup { color: var(--cyan); font-size: 26px; }
  .sizes-sub {
    font: 500 17px/20px "Oswald", Arial, sans-serif; color: var(--cyan); margin-top: 8px;
    white-space: nowrap;
  }
  .size-list { list-style: none; margin-top: 16px; }
  .size-list li {
    position: relative; font: 700 14.5px/18px "Roboto", Arial, sans-serif; color: var(--black);
    margin-bottom: 24px; white-space: nowrap;
  }
  .size-list li::before {
    content: "*"; position: absolute; left: 34px; top: 2px; font-size: 24px; color: var(--cyan);
  }
  .size-list li:last-child::before { left: 28px; }
  .size-list .price { display: block; font-style: italic; font-weight: 500; }
</style>
</head>
<body>
<main class="flyer">
  <svg class="headline" viewBox="0 0 848 600" xmlns="http://www.w3.org/2000/svg" aria-label="Store it, don't ship it, 4-less">
    <rect x="0" y="0" width="848" height="572" fill="var(--yellow)"/>
    <text class="display display-heavy" x="0" y="252" font-size="314" textLength="808" lengthAdjust="spacingAndGlyphs" fill="var(--black)">store it</text>
    <text class="display" x="820" y="272" font-size="330" fill="var(--cyan)">,</text>
    <text class="display display-heavy" x="0" y="571" font-size="390" textLength="752" lengthAdjust="spacingAndGlyphs" fill="var(--black)">4-less</text>
    <text class="display" x="390" y="352" font-size="96" textLength="336" lengthAdjust="spacingAndGlyphs" fill="var(--white)">don’t ship it</text>
  </svg>

  <p class="with-label">with</p>
  <h1>
    <svg class="business-name" viewBox="0 0 848 90" xmlns="http://www.w3.org/2000/svg" aria-label="Tuck It At Bramwood">
      <text x="66" y="78" textLength="714" lengthAdjust="spacingAndGlyphs">TUCK IT AT <tspan class="accent">BRAMWOOD</tspan></text>
    </svg>
  </h1>
  <p class="tagline">convenience, quality, service</p>

  <p class="forward-note">Should you not return to the school we will forward your<br>items in storage to you for a postage fee of + 15.00 CHFs.</p>
  <p class="contact">Contact Tom on <span class="phone">064-293-5527</span><span class="sub">for further enquires</span></p>

  <div class="steps-circle"></div>
  <section class="steps">
    <h2 class="steps-title">Easy as ABC . . .</h2>
    <ol class="step-list">
      <li><span class="letter">A.</span> Contact Us</li>
      <li><span class="letter">B.</span> We deliver</li>
      <li><span class="letter">C.</span> We pick-up &amp; Store</li>
    </ol>
    <p class="slogan">LESS, is the new MORE!</p>
  </section>
  <div class="boxes-photo" role="img" aria-label="Photo of a stack of cardboard moving boxes"></div>

  <div class="sizes-circle"></div>
  <section class="sizes">
    <h2 class="sizes-title">BOX SIZES<sup>*</sup></h2>
    <p class="sizes-sub">(Approx) Weight Limit Price perMonth</p>
    <ul class="size-list">
      <li>41 cm X 34 cm X 26 cm 10 Kilos<span class="price">12 CHFs/per month</span></li>
      <li>48 cm X 43 cm X 35 cm 25 Kilos<span class="price">25 CHFs/per month</span></li>
      <li>Larger sizes and prices available<br>upon request.</li>
    </ul>
  </section>
</main>
</body>
</html>
```